Certified Public Accountant specializing in tax preparation.

I need a business card designed that conveys knowledgeability, trustworthiness and competency. I am a licensed CPA and hold a Master's in taxation. As this is a personal service business, I would like to include my picture on the card.

```html
<!DOCTYPE html>
<html lang="en">
<head>
<meta charset="utf-8">
<title>Daniel Marlow – Licensed CPA Business Card</title>
<link rel="stylesheet" href="https://fonts.googleapis.com/css2?family=Cinzel:wght@500&family=Open+Sans:wght@400&display=swap">
<style>
  :root {
    --page-bg: #e9e7e7;
    --card-bg: #2a2a2a;
    --name-lilac: #dcbfdc;
    --text-white: #f4f2f4;
    --icon-tint: #e6dbe6;
    --photo-light: #f3eef0;
    --photo-pink: #e6bfd2;
    --photo-brown: #6b4a3c;
    --ring: #d9d6d8;
  }
  * { margin: 0; padding: 0; box-sizing: border-box; }
  html, body {
    width: 1200px;
    height: 900px;
    overflow: hidden;
    background: var(--page-bg);
  }
  .business-card {
    position: absolute;
    left: 210px;
    top: 207px;
    width: 780px;
    height: 486px;
    background: var(--card-bg);
    box-shadow: 0 10px 30px rgba(0,0,0,0.18);
  }
  .identity {
    position: absolute;
    left: 44px;
    top: 102px;
  }
  .identity__name {
    font-family: "Cinzel", serif;
    font-weight: 500;
    font-size: 28px;
    letter-spacing: 0.5px;
    color: var(--name-lilac);
    line-height: 1.1;
  }
  .identity__title {
    font-family: "Open Sans", sans-serif;
    font-size: 20px;
    color: var(--text-white);
    margin-top: 2px;
  }
  .contact-list {
    position: absolute;
    left: 44px;
    top: 256px;
    list-style: none;
    font-family: "Open Sans", sans-serif;
    font-size: 21px;
    color: var(--text-white);
  }
  .contact-list__item {
    display: flex;
    align-items: center;
    height: 29px;
  }
  .contact-list__icon {
    width: 18px;
    height: 18px;
    margin-right: 6px;
    fill: var(--icon-tint);
    flex: none;
  }
  .portrait-frame {
    position: absolute;
    left: 342px;
    top: 32px;
    width: 420px;
    height: 420px;
    border-radius: 50%;
    padding: 4px;
    background: var(--ring);
  }
  .portrait {
    width: 100%;
    height: 100%;
    border-radius: 50%;
    background:
      radial-gradient(ellipse 34% 42% at 50% 40%, var(--photo-brown) 0%, rgba(107,74,60,0.6) 55%, transparent 100%),
      radial-gradient(ellipse 55% 30% at 50% 92%, var(--photo-pink) 0%, rgba(230,191,210,0.6) 60%, transparent 100%),
      var(--photo-light);
  }
</style>
</head>
<body>
  <main class="business-card">
    <div class="identity">
      <h1 class="identity__name">DANIEL MARLOW</h1>
      <p class="identity__title">Licensed CPA</p>
    </div>

    <ul class="contact-list">
      <li class="contact-list__item">
        <svg class="contact-list__icon" viewBox="0 0 24 24" aria-hidden="true"><path d="M3 9c0-3 4-5 9-5s9 2 9 5v1.5h-5V8.5c-1-.6-2.5-.9-4-.9s-3 .3-4 .9v2H3z"/><path d="M6 12h12l2 8H4z M12 13.5a3 3 0 1 0 0 6 3 3 0 0 0 0-6z"/></svg>
        044-987 654 321
      </li>
      <li class="contact-list__item">
        <svg class="contact-list__icon" viewBox="0 0 24 24" aria-hidden="true"><path d="M7 2h10a1.5 1.5 0 0 1 1.5 1.5v17A1.5 1.5 0 0 1 17 22H7a1.5 1.5 0 0 1-1.5-1.5v-17A1.5 1.5 0 0 1 7 2zm.5 3v13h9V5zm4.5 14.2a1 1 0 1 0 0 2 1 1 0 0 0 0-2z"/></svg>
        044-987 654 321
      </li>
      <li class="contact-list__item">
        <svg class="contact-list__icon" viewBox="0 0 24 24" aria-hidden="true"><path d="M2 5h20v14H2z" opacity="0.95"/><path d="M2 5l10 8 10-8" fill="none" stroke="#2a2a2a" stroke-width="1.8"/></svg>
        hello@marlowtax.com
      </li>
      <li class="contact-list__item">
        <svg class="contact-list__icon" viewBox="0 0 24 24" aria-hidden="true"><circle cx="12" cy="12" r="10"/><path d="M7 6c2 1 3 3 2 5s-3 2-3 4 2 3 2 5M15 4c-1 2 0 3 2 4s3 3 2 5-3 1-4 3 0 4 1 5" fill="none" stroke="#2a2a2a" stroke-width="1.6"/></svg>
        www.marlowtax.com
      </li>
    </ul>

    <div class="portrait-frame">
      <div class="portrait" role="img" aria-label="Portrait photograph of the accountant in a pink blazer against a light office background"></div>
    </div>
  </main>
</body>
</html>
```